Business card

We need a business card design for our company based in Auckland , New Zealand called 'Kestrel + Design Ltd'. We provide architectural services. We would like to see designs that use the max. three colours (such as white, black, grey) The final design should communicate financial safety and growth."
Also I will provide our company logo. I would like to the logo to be embeded onto our business card.

Target Market(s)

new residential house, alteration & addition & light commericila design & drafting service

Industry/Entity Type

Architecture

Contact Information for Business Card

Company name: kestrel + design Ltd.
Name: Mark Telford
Job title: architectural designer & Design RQC
email address: mark@kdstudio.co.nz
mobile number: 02 5319 6620
web site: www.kdstudio.co.nz

Requirements
Must have
• My project must have..
• - embeded logo (attached company logo)
• I don't have a bigger version for our company logo, but I have one old one, so you can remove the word from it)
• - insert the attached small PDGQ logo & RQC logo
• - creative, simple and clear business card.
• - Max. three colours
Nice to have
• - Here are the samples I would like to share with you: http://www.velmorindex.com/blog/minimalistic-business-card-designs/
• I would like to have my business card like one of the creation.
Should not have
• TBA

```html
<!DOCTYPE html>
<html lang="en">
<head>
<meta charset="utf-8">
<title>Kestrel + Design Ltd — Business Card</title>
<link href="https://fonts.googleapis.com/css2?family=Roboto+Condensed:wght@300;400&display=swap" rel="stylesheet">
<style>
  :root {
    --backdrop: #555555;
    --card-white: #ffffff;
    --card-dark: #3f3f3f;
    --accent: #f7941d;
    --ink: #2b2b2b;
    --faint: #ececec;
    --badge-dark: #1e1e1e;
    --badge-grey: #a7a7a7;
  }
  * { margin: 0; padding: 0; box-sizing: border-box; }
  html, body { width: 1200px; height: 1200px; overflow: hidden; }
  body {
    background: var(--backdrop);
    font-family: "Roboto Condensed", "Arial Narrow", sans-serif;
    position: relative;
  }
  .card {
    position: absolute;
    left: 285px;
    width: 630px;
    height: 357px;
    box-shadow: 0 4px 10px rgba(0,0,0,0.45);
    overflow: hidden;
  }
  .card--front { top: 200px; background: var(--card-white); }
  .card--back { top: 630px; background: var(--card-dark); }

  .identity__bar {
    position: absolute; left: 0; top: 40px;
    width: 13px; height: 69px; background: var(--accent);
  }
  .identity__name {
    position: absolute; left: 33px; top: 44px;
    font-size: 32px; font-weight: 300; color: var(--accent); line-height: 1;
  }
  .identity__title {
    position: absolute; left: 33px; top: 82px;
    font-size: 21px; font-weight: 300; color: var(--ink); line-height: 1;
  }
  .contact__divider {
    position: absolute; left: 369px; top: 42px;
    width: 1px; height: 65px; background: var(--accent);
  }
  .contact__list { list-style: none; position: absolute; left: 390px; top: 38px; }
  .contact__item {
    display: flex; align-items: center; height: 24px;
    font-size: 20px; font-weight: 300; color: var(--ink);
  }
  .contact__icon { width: 18px; height: 18px; margin-right: 10px; flex: none; }

  .front__brand-faint {
    position: absolute; left: 20px; top: 240px;
    font-size: 44px; font-weight: 300; color: var(--faint); line-height: 1;
  }
  .badge--practitioner {
    position: absolute; left: 450px; top: 261px;
    width: 64px; height: 64px; border-radius: 50%; background: var(--badge-dark);
  }
  .badge--membership {
    position: absolute; left: 534px; top: 272px;
    width: 58px; height: 40px; background: var(--badge-grey);
  }

  .back__brand {
    position: absolute; left: 0; right: 0; top: 0; bottom: 0;
    display: flex; align-items: center; justify-content: center; gap: 12px;
  }
  .back__mark { width: 16px; height: 16px; background: var(--accent); }
  .back__name { font-size: 30px; font-weight: 300; color: var(--accent); }
</style>
</head>
<body>
  <section class="card card--front" aria-label="Business card front">
    <div class="identity__bar"></div>
    <h1 class="identity__name">Mark Telford</h1>
    <p class="identity__title">architectural designer &amp; Design RQC</p>

    <div class="contact__divider"></div>
    <ul class="contact__list">
      <li class="contact__item">
        <svg class="contact__icon" viewBox="0 0 18 18"><rect x="1" y="4" width="16" height="11" fill="none" stroke="#f7941d" stroke-width="1.5"/><path d="M1 4 L9 11 L17 4" fill="none" stroke="#f7941d" stroke-width="1.5"/></svg>
        mark@kdstudio.co.nz
      </li>
      <li class="contact__item">
        <svg class="contact__icon" viewBox="0 0 18 18"><rect x="4.5" y="1" width="9" height="16" rx="1.5" fill="none" stroke="#f7941d" stroke-width="1.5"/><line x1="7.5" y1="14.5" x2="10.5" y2="14.5" stroke="#f7941d" stroke-width="1.5"/></svg>
        02 5319 6620
      </li>
      <li class="contact__item">
        <svg class="contact__icon" viewBox="0 0 18 18"><circle cx="9" cy="9" r="7.5" fill="none" stroke="#f7941d" stroke-width="1.3"/><ellipse cx="9" cy="9" rx="3.5" ry="7.5" fill="none" stroke="#f7941d" stroke-width="1.1"/><line x1="1.5" y1="9" x2="16.5" y2="9" stroke="#f7941d" stroke-width="1.1"/><line x1="3" y1="5" x2="15" y2="5" stroke="#f7941d" stroke-width="1"/><line x1="3" y1="13" x2="15" y2="13" stroke="#f7941d" stroke-width="1"/></svg>
        www.kdstudio.co.nz
      </li>
    </ul>

    <div class="front__brand-faint">kestrel + design</div>

    <div class="badge--practitioner" role="img" aria-label="Licensed practitioner badge"></div>
    <div class="badge--membership" role="img" aria-label="PDGQ professional member badge"></div>
  </section>

  <section class="card card--back" aria-label="Business card back">
    <div class="back__brand">
      <span class="back__mark"></span>
      <span class="back__name">kestrel + design Ltd.</span>
    </div>
  </section>
</body>
</html>
```